Financial management business is partnering with chef for a cooking demo and financial workshop j...

We need an promotional invitation/postcard to our event called "Kitchen Table Talks: Cooking Smart All Year Long."

Target Market(s)

55+, seniors

Font styles to use
Serif

Requirements
Must have
• EDDM formatting 6"x9"

```html
<!DOCTYPE html>
<html lang="en">
<head>
<meta charset="utf-8">
<title>Kitchen Table Talks – Postcard</title>
<link href="https://fonts.googleapis.com/css2?family=Libre+Baskerville:wght@400;700&family=Questrial&family=Roboto+Condensed:wght@400;700&display=swap" rel="stylesheet">
<style>
  :root{
    --bg:#dfe6e9;
    --paper:#ffffff;
    --green:#6aaa45;
    --green-dark:#4f8a32;
    --blue:#2e3192;
    --navy:#2b3590;
    --maroon:#6e1139;
    --gold:#d9a035;
    --cream:#fbf8ec;
    --ink:#222222;
    --rule:#8a8a8a;
    --serif:"Libre Baskerville", Georgia, serif;
    --sans:"Questrial", Arial, sans-serif;
    --cond:"Roboto Condensed", "Arial Narrow", sans-serif;
  }
  *{box-sizing:border-box;margin:0;padding:0}
  html,body{width:1200px;height:1200px;overflow:hidden;background:var(--bg)}
  .card{
    position:absolute;width:1003px;height:717px;background:var(--paper);
    transform:scale(0.775);transform-origin:0 0;
    box-shadow:0 2px 8px rgba(0,0,0,.12);
  }
  .card--front{left:211px;top:30px}
  .card--back{left:211px;top:614px}
  .abs{position:absolute}

  /* front */
  .title-block{left:18px;top:18px;width:477px;height:384px;background:var(--green);overflow:hidden}
  .title-block h1{position:absolute;left:22px;top:30px;width:440px;font-family:var(--serif);font-weight:700;
    color:#fff;font-size:41px;line-height:60px;white-space:nowrap}
  .title-rule{position:absolute;left:22px;top:183px;width:436px;height:4px;background:#fff}
  .title-block .subtitle{position:absolute;left:0;top:200px;width:477px;text-align:center;font-family:var(--sans);
    color:#fff;font-size:46px;line-height:55px}
  .produce-band{position:absolute;left:0;bottom:0;width:477px;height:78px;
    background:linear-gradient(180deg,rgba(106,170,69,0) 0%,#5c9a3a 45%,#4c8a2e 100%)}
  .photo{background:linear-gradient(135deg,#5f8f3e 0%,#9bbf6a 35%,#c98a5a 60%,#7a5a3c 100%)}
  .photo--dinner{left:507px;top:18px;width:477px;height:384px}
  .photo--gardener{left:400px;top:412px;width:286px;height:212px;
    background:linear-gradient(160deg,#a9cfe6 0%,#6f9e45 40%,#3f7a2c 75%,#8e3a3a 100%)}
  .details{left:18px;top:412px;width:440px;height:212px}
  .details-text{left:40px;top:452px;font-family:var(--cond);color:#fff}
  .details-row{display:flex;font-size:31px;line-height:38px;white-space:nowrap}
  .details-row .label{font-weight:700;width:104px}
  .details-row .value{font-weight:400}
  .details-row--where{margin-top:24px}
  .details-row--where .label{width:130px}
  .sponsor{left:686px;top:412px;width:298px;height:212px;text-align:center}
  .sponsor .by{font-family:var(--cond);font-size:29px;line-height:36px;color:var(--ink);margin-top:30px}
  .sponsor .brand{font-family:var(--serif);color:var(--navy);font-size:20px;letter-spacing:1.5px;margin-top:30px;
    display:flex;align-items:center;justify-content:center;gap:8px;white-space:nowrap}
  .sponsor .brand .dot{flex:none;width:18px;height:18px;border-radius:50%;background:var(--navy)}
  .footer-band{left:18px;top:634px;width:966px;height:63px;background:var(--green)}

  /* back */
  .bios{left:17px;top:18px;width:527px;height:352px;background:var(--green)}
  .bio{position:absolute;left:13px;width:490px;color:#fff;font-family:var(--cond)}
  .bio h2{font-size:18.5px;font-weight:700;letter-spacing:.1px;line-height:22px}
  .bio p{width:368px;margin-top:9px;font-size:14px;font-weight:700;line-height:19.2px;text-align:justify}
  .bio--planner{top:14px}
  .bio--chef{top:174px}
  .portrait{position:absolute;width:122px;height:122px;border-radius:50%;border:3px solid var(--gold);
    background:linear-gradient(160deg,#9aa8a0 0%,#55605a 60%,#2d3440 100%)}
  .portrait--planner{left:396px;top:27px}
  .portrait--chef{left:396px;top:206px;background:linear-gradient(160deg,#b9b3aa 0%,#6f655a 55%,#f2f2f2 100%)}
  .promo{left:17px;top:370px;width:527px;height:347px;background:var(--cream)}
  .promo-title{position:absolute;left:12px;top:24px;width:190px;text-align:center}
  .promo-title h3{font-family:var(--serif);color:var(--gold);font-size:19px;line-height:26px;font-weight:400;white-space:nowrap}
  .promo-title .rule{height:2px;background:var(--gold);margin:8px 4px 8px}
  .promo-title .sub{font-family:var(--sans);color:var(--gold);font-size:20px;line-height:23px}
  .promo-copy{position:absolute;left:212px;top:10px;width:300px;font-family:var(--cond);font-weight:700;
    color:var(--green-dark);font-size:14px;line-height:19.2px;text-align:justify}
  .raffle{left:25px;top:528px;width:316px;height:100px}
  .raffle-text{left:67px;top:536px;width:272px;text-align:center;color:#fff;font-family:var(--cond);
    font-weight:700;font-size:16px;line-height:21.5px}
  .photo--kitchen{left:338px;top:528px;width:206px;height:170px;
    background:linear-gradient(135deg,#e9e6e0 0%,#c8c3bb 40%,#4a4a4e 75%,#8fa3c0 100%)}
  .partner{left:100px;top:642px;width:170px;text-align:center;font-family:var(--cond);font-weight:700;
    color:var(--ink);font-size:14px;letter-spacing:.5px}
  .partner .dot{display:block;width:28px;height:28px;border-radius:50%;background:var(--maroon);margin:0 auto 6px}
  .stamp{left:855px;top:37px;width:108px;height:123px;border:2px solid var(--rule)}
  .address-line{left:568px;width:400px;height:2px;background:var(--rule)}
</style>
</head>
<body>

<section class="card card--front" aria-label="Postcard front">
  <div class="abs title-block">
    <h1>KITCHEN TABLE<br>TALKS</h1>
    <div class="title-rule"></div>
    <p class="subtitle">Cooking Smart<br>All Year Long</p>
    <div class="produce-band" role="img" aria-label="Band of fresh garden vegetables and fruit"></div>
  </div>
  <div class="abs photo photo--dinner" role="img" aria-label="Friends sharing a fresh summer meal at an outdoor table"></div>

  <div class="abs photo photo--gardener" role="img" aria-label="Woman picking berries in a sunny garden"></div>
  <svg class="abs details" width="440" height="212" viewBox="0 0 440 212" aria-hidden="true">
    <polygon points="0,0 418,0 388,106 418,212 0,212" fill="var(--blue)"/>
    <polyline points="0,10 400,10 373,106 400,202 0,202" fill="none" stroke="#fff" stroke-width="2" stroke-dasharray="10 6"/>
  </svg>
  <div class="abs details-text">
    <div class="details-row"><span class="label">WHEN:</span><span class="value">Tuesday, July 23rd</span></div>
    <div class="details-row"><span class="label"></span><span class="value">&nbsp;&nbsp;&nbsp;&nbsp;at 12:30 p.m.</span></div>
    <div class="details-row details-row--where"><span class="label">WHERE:</span><span class="value">Ashford Hall</span></div>
  </div>

  <div class="abs sponsor">
    <p class="by">Sponsored by<br>Harlow Financial</p>
    <p class="brand"><span class="dot"></span>HARLOW FINANCIAL</p>
  </div>
  <div class="abs footer-band"></div>
</section>

<section class="card card--back" aria-label="Postcard back">
  <div class="abs bios">
    <div class="bio bio--planner">
      <h2>A CERTIFIED FINANCIAL PLANNER YOU CAN TRUST</h2>
      <p>Glen Harlow is a Certified Financial Planner, specializing in asset management of IRA, retirement, investment, and trust accounts. Harlow Advisors, LLC is an independent Registered Investment Advisor with low cost, commission free business model. Concierge level service is provided to Willow Creek Commons residents.</p>
    </div>
    <div class="portrait portrait--planner" role="img" aria-label="Portrait of the financial planner"></div>
    <div class="bio bio--chef">
      <h2>A CERTIFIED FINANCIAL PLANNER YOU CAN TRUST</h2>
      <p>Chef Owen Bracken is a formally trained chef with over 15 years of experience. He started Hearth Chefs Brookfield, a meal service that connects seniors with licensed, professional chefs who prepare high-quality, affordable, and nutritious meals in the home. Owen is so pleased to have found an opportunity to share his passion for food and connect with local Seniors.</p>
    </div>
    <div class="portrait portrait--chef" role="img" aria-label="Portrait of the chef"></div>
  </div>

  <div class="abs promo">
    <div class="promo-title">
      <h3>KITCHEN TABLE<br>TALKS</h3>
      <div class="rule"></div>
      <p class="sub">Cooking Smart<br>All Year Long</p>
    </div>
    <p class="promo-copy">Learn from Chef Owen Bracken how to build a menu full of flavor, nutrition, and seasonal ingredients with ease. Followed by a financial workshop where Glen Harlow, Certified Financial Planner, will have some fresh investment ideas to go along with your farm-to-table meal. Glen encourages any questions you may have.</p>
  </div>

  <svg class="abs raffle" width="316" height="100" viewBox="0 0 316 100" aria-hidden="true">
    <polygon points="14,0 316,0 316,100 0,100 28,50" fill="var(--maroon)"/>
  </svg>
  <p class="abs raffle-text">Enter a raffle to win the services of Chef Owen who will work with you to design a meal plan of 10-12 servings that addresses your dietary need</p>
  <div class="abs photo photo--kitchen" role="img" aria-label="Chef cooking for a senior woman in a home kitchen"></div>
  <div class="abs partner"><span class="dot"></span>HEARTH CHEFS</div>

  <div class="abs stamp"></div>
  <div class="abs address-line" style="top:362px"></div>
  <div class="abs address-line" style="top:418px"></div>
  <div class="abs address-line" style="top:470px"></div>
  <div class="abs address-line" style="top:523px"></div>
</section>

</body>
</html>
```